Need Business Card for our Real Estate Business with Sales Executive's Picture

PANTONE 484 C ( RED)

PANTONE 2766 C ( BLUE

Industry/Entity Type

Real Estate

Contact Information for Business Card

Name, Mobile, email, & picture of Person
Agency Phone, address, Web address

Requirements
Must have
• Our Logo Colours, Agent Picture,

```html
<!DOCTYPE html>
<html lang="en">
<head>
<meta charset="utf-8">
<title>Dunmore Real Estate – Business Card</title>
<link rel="stylesheet" href="https://fonts.googleapis.com/css2?family=Arimo:wght@400;700&display=swap">
<style>
  :root {
    --navy: #0b1640;
    --red: #7a1420;
    --white: #ffffff;
    --ink: #1b2450;
    --muted: #4a4f63;
    --backdrop: #d4d4d6;
  }
  * { box-sizing: border-box; margin: 0; padding: 0; }
  html, body { width: 1200px; height: 800px; overflow: hidden; }
  body {
    background: var(--backdrop);
    font-family: "Arimo", Arial, sans-serif;
    display: flex;
    align-items: center;
    justify-content: center;
    gap: 40px;
  }
  .card {
    width: 520px;
    height: 298px;
    position: relative;
    overflow: hidden;
    box-shadow: 0 6px 18px rgba(0,0,0,0.18);
  }
  /* Front */
  .card-front { background: var(--white); }
  .portrait-frame {
    position: absolute;
    left: 44px; top: 62px;
    width: 150px; height: 150px;
    border: 1.5px solid var(--navy);
    padding: 6px;
    background: var(--white);
  }
  .portrait {
    width: 100%; height: 100%;
    background: linear-gradient(180deg, #f3f1ef 0%, #e8e2dc 40%, #2c3f8a 70%, #1e2e6e 100%);
  }
  .divider {
    position: absolute;
    left: 238px; top: 72px;
    width: 1.5px; height: 118px;
    background: var(--navy);
  }
  .details {
    position: absolute;
    left: 262px; top: 66px;
    color: var(--muted);
    font-size: 11px;
    line-height: 1.45;
  }
  .name {
    font-size: 17px;
    font-weight: 700;
    color: var(--ink);
    letter-spacing: 0.3px;
    line-height: 1.1;
  }
  .role { margin-bottom: 8px; }
  .address { margin-bottom: 6px; }
  .contact-list { list-style: none; }
  .contact-list li { display: flex; align-items: center; gap: 8px; }
  .contact-list svg { width: 9px; height: 9px; fill: var(--navy); flex: none; }
  .bottom-band {
    position: absolute;
    left: 0; right: 0; bottom: 0;
    height: 7px;
    display: flex;
  }
  .bottom-band .band-navy { flex: 0 0 58%; background: var(--navy); }
  .bottom-band .band-red { flex: 1; background: var(--red); }
  /* Back */
  .card-back {
    background: var(--navy);
    display: flex;
    align-items: center;
    justify-content: center;
  }
  .brand {
    display: flex;
    align-items: center;
    gap: 14px;
    color: var(--white);
    font-size: 30px;
    font-weight: 400;
    letter-spacing: 3px;
    text-transform: uppercase;
  }
  .brand-mark {
    width: 14px; height: 14px;
    background: var(--white);
  }
</style>
</head>
<body>
  <section class="card card-front" aria-label="Business card front">
    <div class="portrait-frame">
      <div class="portrait" role="img" aria-label="Portrait photo of the sales executive in a blue suit"></div>
    </div>
    <div class="divider"></div>
    <div class="details">
      <p class="name">DANIEL BROOKS</p>
      <p class="role">Managing Director</p>
      <p class="address">Via Colle Verde,<br>148, 12030 Lagnasco (CN)</p>
      <ul class="contact-list">
        <li><svg viewBox="0 0 10 10"><path d="M2 0.5l2 2-1 1.2c.6 1.3 1.6 2.3 2.9 2.9l1.2-1 2 2-1.3 1.9C4 9.2 0.8 6 0.5 1.8z"/></svg>+852 2419 0615</li>
        <li><svg viewBox="0 0 10 10"><rect x="1" y="3" width="8" height="5" rx="1"/><rect x="3" y="0.5" width="4" height="3"/></svg>+852 2419 0677</li>
        <li><svg viewBox="0 0 10 10"><path d="M0.5 2h9v6h-9z M1.5 3l3.5 2.5 3.5-2.5" fill="none" stroke="#0b1640" stroke-width="1"/></svg>info@dunmorerealestate.com</li>
        <li><svg viewBox="0 0 10 10"><circle cx="5" cy="5" r="4.2" fill="none" stroke="#0b1640" stroke-width="1"/><path d="M1 5h8M5 1c-2 2.5-2 5.5 0 8M5 1c2 2.5 2 5.5 0 8" fill="none" stroke="#0b1640" stroke-width="0.8"/></svg>www.dunmorerealestate.com</li>
      </ul>
    </div>
    <div class="bottom-band"><span class="band-navy"></span><span class="band-red"></span></div>
  </section>

  <section class="card card-back" aria-label="Business card back">
    <p class="brand"><span class="brand-mark"></span>Dunmore Real Estate</p>
  </section>
</body>
</html>
```